Reaching the Root: Reasoning in Clinical Choice-Making

I'd like a cover that looks like it would fit on the shelf next to "The Symptom Mirage" by Harold Vintner, "The Fall of Forgetting" by Carl Mortenson, "Meal Mend" by Neil Forsby, "The Energy Renewal Plan" by Owen Prichardson or "The Gland Renewal Plan" by the same or "The Cortex Renewal Plan" by the same ... either text only (with some interesting fonts that make the title stand out, and the subtitle smaller) or a relevant image, though I'm not entirely sure what that would be since this is a book about big-picture medical decision making.
Author name is Dr Miriam Oakhurst, NMD
I'll eventually request an e-book, paperback, and audio cover from the winner...

Target Market(s)

practicing physicians

Industry/Entity Type

medicine

Requirements
Must have
• look similar to other books in the genre

```html
<!DOCTYPE html>
<html lang="en">
<head>
<meta charset="utf-8">
<title>Reaching the Root: Reasoning in Clinical Choice-Making</title>
<link rel="stylesheet" href="https://fonts.googleapis.com/css2?family=Bebas+Neue&family=Libre+Franklin:wght@400;700&display=swap">
<style>
  :root {
    --paper: #efebe4;
    --navy: #09264a;
    --navy-mid: #154573;
    --subtitle-blue: #1e5a8e;
  }
  html, body {
    margin: 0;
    padding: 0;
    width: 800px;
    height: 1200px;
    overflow: hidden;
    background: var(--paper);
  }
  .cover {
    position: relative;
    width: 800px;
    height: 1200px;
    background: var(--paper);
  }
  .cover-art {
    position: absolute;
    inset: 0;
  }
  .title-word {
    font-family: "Bebas Neue", "Oswald", sans-serif;
  }
  .title-top, .title-joiner { fill: var(--navy); }
  .title-main { fill: url(#title-fade); }
  .rule { fill: var(--navy); }
  .subtitle {
    position: absolute;
    left: 62px;
    top: 843px;
    margin: 0;
    font-family: "Libre Franklin", "Franklin Gothic Medium", sans-serif;
    font-weight: 700;
    font-size: 40px;
    line-height: 46px;
    color: var(--subtitle-blue);
    text-transform: uppercase;
  }
  .subtitle span { display: block; }
  .author {
    position: absolute;
    left: 0;
    right: 0;
    top: 1114px;
    margin: 0;
    text-align: center;
    font-family: "Libre Franklin", "Franklin Gothic Book", sans-serif;
    font-weight: 400;
    font-size: 40px;
    letter-spacing: 3px;
    color: var(--navy);
    text-transform: uppercase;
  }
</style>
</head>
<body>
  <main class="cover">
    <svg class="cover-art" width="800" height="1200" viewBox="0 0 800 1200">
      <defs>
        <linearGradient id="title-fade" x1="0" y1="401" x2="0" y2="1000" gradientUnits="userSpaceOnUse">
          <stop offset="0" stop-color="#09264a"/>
          <stop offset="0.5" stop-color="#154573"/>
          <stop offset="1" stop-color="#154573"/>
        </linearGradient>
        <radialGradient id="emblem-glow" cx="0.5" cy="0.5" r="0.5">
          <stop offset="0" stop-color="#154573" stop-opacity="0.85"/>
          <stop offset="0.6" stop-color="#154573" stop-opacity="0.45"/>
          <stop offset="1" stop-color="#efebe4" stop-opacity="0"/>
        </radialGradient>
      </defs>

      <text class="title-word title-top" x="59" y="262" font-size="262" textLength="681" lengthAdjust="spacingAndGlyphs">REACHING</text>

      <rect class="rule" x="52" y="332" width="266" height="5"/>
      <text class="title-word title-joiner" x="400" y="365" font-size="94" text-anchor="middle">THE</text>
      <rect class="rule" x="482" y="334" width="264" height="5"/>

      <text class="title-word title-main" x="59" y="792" font-size="545" textLength="681" lengthAdjust="spacingAndGlyphs">ROOT</text>

      <rect class="question-emblem" x="445" y="800" width="300" height="235" fill="url(#emblem-glow)" role="img" aria-label="Illustration: a large question mark whose curve forms a head in profile, in deep blue"/>

      <rect class="rule" x="66" y="1072" width="674" height="3"/>
    </svg>

    <h2 class="subtitle">
      <span>Reasoning in</span>
      <span>Clinical</span>
      <span>Choice-Making</span>
    </h2>

    <p class="author">Dr Miriam Oakhurst, NMD</p>
  </main>
</body>
</html>
```